依頼詳細
現状、施工した場所に施工済ステッカーを貼っているのですが、
今回施工をしたホテル様の要望で、フロントや客室にお客様へ向けたアピールできるチラシなどが欲しいといわれました。
ホテルのフロント・客室の卓上におけるものや・車内に貼れるものなので
年賀状サイズくらいで検討しています。

イメージは
・主成分でもある青森ヒバをモチーフにしたもの
・一目でわかる安心感が伝わるもの
・100%天然成分で安心安全
・キャッチコピーは『植物の力で抗菌中!』

記載項目
ヴェルトナ産業株式会社 0120-387-905
Lumiva Plus
サイズ
年賀状サイズくらい
ページ数
片面
希望イメージ
シンプル 複雑
単色 カラフル
暗い 明るい
日常 高級
遊び心 厳粛
未来的 伝統的
女性的 男性的
希望する色
緑系、青系
納品ファイル
• 高解像度JPG (.jpg)
補足説明
当社が使用しているチラシです。
■ 選んだ理由

どの候補者もとても良かったですが、
こちらはどのシチュエーションでもあうようなデザインかつ
柔らかい印象で、安心感を与えてくれるようなデザインなので決めました。

■ 提案者全員のお礼・コメント

とても素晴らしいデザインばかりでかなり迷いました。
予算があれば他の候補者も当選sて他のですが。
今後は社のチラシなども作成予定ですので、
またお願いするかと思います。
宜しくお願い致します。

```html
<!DOCTYPE html>
<html lang="ja">
<head>
<meta charset="utf-8">
<title>Lumiva Plus 施工済み</title>
<link rel="stylesheet" href="https://fonts.googleapis.com/css2?family=M+PLUS+Rounded+1c:wght@400;500;700;800&family=Montserrat:wght@500&display=swap">
<style>
  :root {
    --mint: #dcefeb;
    --teal: #1f7f86;
    --teal-dark: #17666d;
    --leaf-light: #6f9a5c;
    --leaf-mid: #3f6b33;
    --leaf-dark: #1f3a1c;
    --white: #ffffff;
  }
  html, body { margin: 0; padding: 0; overflow: hidden; }
  body { width: 810px; height: 1200px; background: var(--white); }
  .flyer {
    position: relative; width: 810px; height: 1200px; overflow: hidden;
    font-family: "M PLUS Rounded 1c", sans-serif;
    background: var(--mint);
  }
  .foliage-photo {
    position: absolute; left: 0; top: 310px; width: 810px; height: 890px;
    background:
      radial-gradient(ellipse at 30% 45%, var(--leaf-light) 0%, transparent 55%),
      radial-gradient(ellipse at 80% 30%, #5e8a4a 0%, transparent 50%),
      linear-gradient(180deg, #4f7c3f 0%, var(--leaf-mid) 45%, var(--leaf-dark) 100%);
  }
  .tagline-pill {
    position: absolute; left: 50%; top: 26px; transform: translateX(-50%);
    background: var(--white); color: var(--teal);
    font-size: 25px; font-weight: 500; letter-spacing: 1px;
    padding: 4px 34px; border-radius: 30px; white-space: nowrap;
  }
  .brand-name {
    position: absolute; left: 0; right: 0; top: 92px; text-align: center;
    font-family: "Montserrat", sans-serif; font-weight: 500;
    font-size: 78px; color: var(--teal); letter-spacing: 1px;
  }
  .status-circle {
    position: absolute; left: 135px; top: 210px; width: 540px; height: 540px;
    border-radius: 50%; background: var(--white);
  }
  .status-text { position: absolute; left: 0; right: 0; text-align: center; color: var(--teal); font-weight: 700; }
  .status-text.scope { top: 232px; font-size: 40px; }
  .status-text.action { top: 286px; font-size: 64px; }
  .status-text.done { font-size: 134px; font-weight: 800; line-height: 1; letter-spacing: 6px; }
  .status-text.done.first { top: 380px; }
  .status-text.done.second { top: 526px; }
  .benefit-row {
    position: absolute; left: 0; right: 0; top: 826px;
    display: flex; justify-content: center; gap: 22px;
  }
  .benefit {
    width: 196px; height: 102px; border: 4px solid var(--white); border-radius: 52px;
    box-sizing: border-box; color: var(--white); font-size: 52px; font-weight: 700;
    display: flex; align-items: center; justify-content: center; letter-spacing: 2px;
  }
  .promise {
    position: absolute; left: 0; right: 0; top: 926px; text-align: center;
    color: var(--white); font-size: 50px; font-weight: 700; letter-spacing: 1px;
  }
  .catchcopy {
    position: absolute; left: 0; right: 0; top: 1000px; text-align: center;
    color: var(--white); font-size: 27px; font-weight: 500;
  }
  .company {
    position: absolute; left: 0; right: 0; top: 1082px; text-align: center;
    color: var(--white); font-size: 24px; font-weight: 400;
  }
  .phone {
    position: absolute; left: 0; right: 0; top: 1122px; text-align: center;
    color: var(--white); font-size: 30px; font-weight: 500;
    display: flex; justify-content: center; align-items: center; gap: 6px;
  }
</style>
</head>
<body>
<div class="flyer">
  <div class="foliage-photo" role="img" aria-label="青森ヒバの葉が茂る緑の写真"></div>

  <div class="tagline-pill">青森ヒバ由来の抗菌コート</div>
  <div class="brand-name">Lumiva Plus</div>

  <div class="status-circle"></div>
  <div class="status-text scope">ホテル全室</div>
  <div class="status-text action">コーティング</div>
  <div class="status-text done first">施工</div>
  <div class="status-text done second">済み</div>

  <div class="benefit-row">
    <div class="benefit">除菌</div>
    <div class="benefit">抗菌</div>
    <div class="benefit">消臭</div>
  </div>
  <div class="promise">100%天然成分で安心安全</div>
  <div class="catchcopy">植物の力で抗菌中!</div>

  <div class="company">ヴェルトナ産業株式会社</div>
  <div class="phone">
    <svg width="26" height="26" viewBox="0 0 24 24" aria-hidden="true">
      <path fill="#ffffff" d="M6.6 10.8a15.1 15.1 0 0 0 6.6 6.6l2.2-2.2a1 1 0 0 1 1-.25 11.4 11.4 0 0 0 3.6.57 1 1 0 0 1 1 1V20a1 1 0 0 1-1 1A17 17 0 0 1 3 4a1 1 0 0 1 1-1h3.5a1 1 0 0 1 1 1c0 1.25.2 2.45.57 3.57a1 1 0 0 1-.25 1z"/>
    </svg>
    <span>0120-387-905</span>
  </div>
</div>
</body>
</html>
```